Business Card for an IT professional services company
Lakeshore Datavault Inc.
Business Card for an IT professional services company - Information Technology
Creative Brief
Professional
Martin Keswell
President
2718 5th Avenue SE Calgary, Alberta T2H 4B7
mart@lakeshoredatavault.example
www.lakeshoredatavault.example

```html
<!DOCTYPE html>
<html lang="en">
<head>
<meta charset="utf-8">
<title>Lakeshore Datavault – Business Card</title>
<link rel="stylesheet" href="https://fonts.googleapis.com/css2?family=Roboto:wght@300;400;500&display=swap">
<style>
  :root {
    --bg: #d9dadb;
    --card: #ffffff;
    --brand-blue: #1f5fa8;
    --ink-gray: #5f6163;
    --bar-gray: #8a8c8f;
    --shadow: rgba(0, 0, 0, 0.18);
  }
  * { margin: 0; padding: 0; box-sizing: border-box; }
  html, body { width: 1200px; height: 895px; overflow: hidden; }
  body {
    background: var(--bg);
    font-family: "Roboto", Arial, sans-serif;
    position: relative;
  }
  .card {
    position: absolute;
    width: 525px;
    height: 300px;
    background: var(--card);
    box-shadow: 0 6px 18px var(--shadow);
    overflow: hidden;
  }
  .card--front { left: 50px; top: 298px; }
  .card--back  { left: 625px; top: 298px; }

  .brand {
    position: absolute;
    display: flex;
    align-items: center;
    gap: 10px;
    color: var(--brand-blue);
    font-weight: 400;
    white-space: nowrap;
  }
  .brand__square { width: 18px; height: 18px; background: var(--brand-blue); }
  .card--front .brand { left: 30px; top: 30px; font-size: 23px; }
  .card--back .brand { left: 50%; top: 50%; transform: translate(-50%, -50%); font-size: 28px; }
  .card--back .brand__square { width: 22px; height: 22px; }

  .person { position: absolute; left: 150px; top: 86px; }
  .person__name {
    color: var(--brand-blue);
    font-size: 17px;
    font-weight: 400;
    letter-spacing: 1.5px;
    text-transform: uppercase;
  }
  .person__title {
    color: var(--ink-gray);
    font-size: 9px;
    letter-spacing: 1.4px;
    text-transform: uppercase;
    margin-top: 2px;
  }

  .contact {
    position: absolute;
    display: flex;
    align-items: flex-start;
    gap: 8px;
    color: var(--ink-gray);
    font-size: 11px;
    line-height: 1.45;
    font-weight: 400;
  }
  .contact svg { flex: none; margin-top: 1px; }
  .contact--address { left: 150px; top: 134px; }
  .contact--web { left: 28px; top: 216px; }
  .contact-list { position: absolute; left: 318px; top: 186px; }
  .contact-list .contact { position: static; margin-bottom: 4px; }

  .footer-bar { position: absolute; left: 0; bottom: 30px; width: 525px; height: 12px; }
</style>
</head>
<body>

<section class="card card--front" aria-label="Business card front">
  <div class="brand">
    <span class="brand__square"></span>
    <span class="brand__name">Lakeshore Datavault</span>
  </div>

  <div class="person">
    <p class="person__name">Martin Keswell</p>
    <p class="person__title">President</p>
  </div>

  <div class="contact contact--address">
    <svg width="10" height="14" viewBox="0 0 10 14" aria-hidden="true">
      <path d="M5 0C2.2 0 0 2.2 0 5c0 3.6 5 9 5 9s5-5.4 5-9c0-2.8-2.2-5-5-5zm0 7a2 2 0 1 1 0-4 2 2 0 0 1 0 4z" fill="var(--brand-blue)"/>
    </svg>
    <p>2718 5th Avenue SE<br>Calgary, Alberta T2H 4B7</p>
  </div>

  <div class="contact contact--web">
    <svg width="12" height="12" viewBox="0 0 12 12" aria-hidden="true">
      <circle cx="6" cy="6" r="6" fill="var(--brand-blue)"/>
    </svg>
    <p>www.lakeshoredatavault.example</p>
  </div>

  <div class="contact-list">
    <div class="contact">
      <svg width="11" height="12" viewBox="0 0 11 12" aria-hidden="true">
        <rect x="0.75" y="0.75" width="9.5" height="10.5" rx="1.5" fill="none" stroke="var(--ink-gray)" stroke-width="1.5"/>
      </svg>
      <p>403 555 0147</p>
    </div>
    <div class="contact">
      <svg width="11" height="12" viewBox="0 0 11 12" aria-hidden="true">
        <rect x="2" y="0.75" width="7" height="10.5" rx="1.2" fill="none" stroke="var(--ink-gray)" stroke-width="1.5"/>
      </svg>
      <p>403 555 0148</p>
    </div>
    <div class="contact">
      <svg width="11" height="12" viewBox="0 0 11 12" aria-hidden="true">
        <rect x="0.75" y="2" width="9.5" height="8" fill="none" stroke="var(--ink-gray)" stroke-width="1.3"/>
        <path d="M0.75 2.5L5.5 6.5L10.25 2.5" fill="none" stroke="var(--ink-gray)" stroke-width="1.3"/>
      </svg>
      <p>mart@lakeshoredatavault.example</p>
    </div>
  </div>

  <svg class="footer-bar" viewBox="0 0 525 12" aria-hidden="true">
    <polygon points="0,0 330,0 320,12 0,12" fill="var(--brand-blue)"/>
    <polygon points="334,0 525,0 525,12 324,12" fill="var(--bar-gray)"/>
  </svg>
</section>

<section class="card card--back" aria-label="Business card back">
  <div class="brand">
    <span class="brand__square"></span>
    <span class="brand__name">Lakeshore Datavault</span>
  </div>
</section>

</body>
</html>
```